2 Redfern Pike Auto Care Banners

Looking to have two pull up banners designed - each 33.5 x 80

First banner- Scheduled Maintenance, Diagnostics, Inspections
Voted Top Pick Marbury 3 years in a row!

Second banner- Brakes, Tires, General Auto Service
Include the 3 TPM logos
2019, 2018, 2017

```html
<!DOCTYPE html>
<html lang="en">
<head>
<meta charset="utf-8">
<title>Redfern Pike Auto Care – Pull Up Banners</title>
<link rel="stylesheet" href="https://fonts.googleapis.com/css2?family=Fjalla+One&family=Jost:wght@400&family=Oswald:wght@500&display=swap">
<style>
  :root {
    --navy: #404f77;
    --navy-text: #3a4770;
    --gold: #bdb55a;
    --panel: #f2f2f2;
    --placeholder-light: #cfcfcf;
    --placeholder-dark: #9c9c9c;
    --backdrop: #e4e4e4;
    --white: #ffffff;
  }
  * { margin: 0; padding: 0; box-sizing: border-box; }
  html, body { width: 1200px; height: 1050px; overflow: hidden; }
  body { background: var(--backdrop); position: relative; }

  .banner {
    position: absolute;
    top: 75px;
    width: 376px;
    height: 900px;
    background: var(--panel);
    overflow: hidden;
    box-shadow: 0 6px 18px rgba(0,0,0,0.12);
  }
  .banner--maintenance { left: 170px; }
  .banner--repairs { left: 654px; }

  .banner__art { position: absolute; inset: 0; width: 376px; height: 900px; }

  .brand-name {
    position: absolute;
    top: 40px;
    left: 0;
    width: 100%;
    text-align: center;
    font-family: "Oswald", sans-serif;
    font-weight: 500;
    font-size: 40px;
    line-height: 46px;
    color: var(--gold);
    letter-spacing: 1px;
  }

  .services {
    position: absolute;
    left: 0;
    width: 100%;
    text-align: center;
    list-style: none;
    font-family: "Fjalla One", sans-serif;
    color: var(--navy-text);
    font-size: 38px;
    line-height: 42px;
    letter-spacing: 0.5px;
  }
  .services--maintenance { top: 218px; }
  .services--repairs { top: 224px; }
  .service { display: block; }
  .star-row {
    display: block;
    color: var(--gold);
    font-size: 13px;
    line-height: 13px;
    letter-spacing: 18px;
    padding-left: 18px;
    margin: 20px 0 22px;
  }

  .award {
    position: absolute;
    right: 28px;
    top: 778px;
    width: 76px;
    text-align: center;
  }
  .award__note {
    font-family: "Jost", sans-serif;
    font-size: 6px;
    line-height: 7px;
    color: var(--white);
  }
  .award__badge {
    display: block;
    width: 66px;
    height: 36px;
    margin: 4px auto 0;
    background: var(--white);
  }

  .award-row {
    position: absolute;
    right: 26px;
    top: 782px;
    display: flex;
    gap: 6px;
  }
  .award-row__badge {
    display: block;
    width: 30px;
    height: 30px;
    background: var(--white);
  }

  .web-address {
    position: absolute;
    left: 0;
    width: 100%;
    text-align: center;
    font-family: "Jost", sans-serif;
    font-weight: 400;
    font-size: 26px;
    color: var(--white);
    letter-spacing: 0.3px;
  }
  .banner--maintenance .web-address { top: 836px; }
  .banner--repairs .web-address { top: 842px; }
</style>
</head>
<body>

<section class="banner banner--maintenance">
  <svg class="banner__art" viewBox="0 0 376 900">
    <defs>
      <linearGradient id="car-placeholder" x1="0" y1="0" x2="0" y2="1">
        <stop offset="0" stop-color="var(--placeholder-light)"/>
        <stop offset="1" stop-color="var(--placeholder-dark)"/>
      </linearGradient>
    </defs>
    <path class="header-band" d="M0 0 H376 V170 C250 150 110 180 0 232 Z" fill="var(--navy)"/>
    <path class="header-accent" d="M0 232 C110 180 250 150 376 170 V192 C250 172 120 195 0 240 Z" fill="var(--gold)"/>
    <path class="photo-area" role="img" aria-label="Photo of a glossy black car, front and side" d="M0 535 H376 V690 C280 752 150 786 0 788 Z" fill="url(#car-placeholder)"/>
    <path class="footer-accent" d="M0 788 C150 786 280 752 376 690 V712 C280 772 150 812 0 818 Z" fill="var(--gold)"/>
    <path class="footer-band" d="M0 818 C150 812 280 772 376 712 V900 H0 Z" fill="var(--navy)"/>
  </svg>

  <p class="brand-name">Redfern Pike<br>Auto Care</p>

  <ul class="services services--maintenance">
    <li class="service">SCHEDULED<br>MAINTENANCE</li>
    <li class="star-row" aria-hidden="true">★★★★★</li>
    <li class="service">DIAGNOSTICS</li>
    <li class="star-row" aria-hidden="true">★★★★★</li>
    <li class="service">INSPECTIONS</li>
  </ul>

  <div class="award">
    <p class="award__note">Voted Top Pick Marbury<br>3 years in a row!</p>
    <span class="award__badge" aria-hidden="true"></span>
  </div>

  <p class="web-address">www.redfernpikeauto.com</p>
</section>

<section class="banner banner--repairs">
  <svg class="banner__art" viewBox="0 0 376 900">
    <defs>
      <linearGradient id="tire-placeholder" x1="0" y1="0" x2="0" y2="1">
        <stop offset="0" stop-color="var(--placeholder-light)"/>
        <stop offset="1" stop-color="var(--placeholder-dark)"/>
      </linearGradient>
    </defs>
    <path class="header-band" d="M0 0 H376 V140 C250 140 110 180 0 245 Z" fill="var(--navy)"/>
    <path class="header-accent" d="M0 245 C110 180 250 140 376 140 V168 C250 168 120 200 0 256 Z" fill="var(--gold)"/>
    <path class="photo-area" role="img" aria-label="Photo of a car tire on an alloy wheel" d="M0 548 H376 V740 C280 780 150 795 0 790 Z" fill="url(#tire-placeholder)"/>
    <path class="footer-accent" d="M0 790 C150 795 280 780 376 740 V760 C280 800 150 820 0 818 Z" fill="var(--gold)"/>
    <path class="footer-band" d="M0 818 C150 820 280 800 376 760 V900 H0 Z" fill="var(--navy)"/>
  </svg>

  <p class="brand-name">Redfern Pike<br>Auto Care</p>

  <ul class="services services--repairs">
    <li class="service">BRAKES</li>
    <li class="star-row" aria-hidden="true">★★★★★</li>
    <li class="service">TIRES</li>
    <li class="star-row" aria-hidden="true">★★★★★</li>
    <li class="service">GENERAL AUTO<br>SERVICE</li>
  </ul>

  <div class="award-row" aria-hidden="true">
    <span class="award-row__badge"></span>
    <span class="award-row__badge"></span>
    <span class="award-row__badge"></span>
  </div>

  <p class="web-address">www.redfernpikeauto.com</p>
</section>

</body>
</html>
```